Business Card Design

I want a non fussy clear design. I like Vintage, Retro writing for the main name as it will be a banner for the roof sign.
Company name, address and ph no. I would also like a unisex symbol small in the corner of the card. The colour of the card does not have to be blue. But I do want a bright clean clear card. A head sillohette small in the other corner possibly.

Industry/Entity Type

Business

Contact Information for Business Card

Kestra Hair Design
318 Marlowe Road, Pennick
Ph (09) 4162093

Requirements
Must have
• The back of the card must have appointment time, date dont worry about the location as its obviously on the front of the card

```html
<!DOCTYPE html>
<html lang="en">
<head>
<meta charset="utf-8">
<title>Kestra Hair Design – Business Card</title>
<link rel="stylesheet" href="https://fonts.googleapis.com/css2?family=Varela+Round&family=Arimo:wght@400;700&display=swap">
<style>
  :root {
    --sheet: #ffffff;
    --card-light: #6e6b69;
    --card-mid: #4b4846;
    --card-dark: #262220;
    --ink-light: #ffffff;
    --silhouette: #8a8886;
    --ink-dark: #111111;
    --crop: #333333;
  }
  * { margin: 0; padding: 0; box-sizing: border-box; }
  html, body {
    width: 1200px; height: 383px; overflow: hidden; background: var(--sheet);
  }
  .print-sheet { position: relative; width: 1200px; height: 383px; }

  .crop-marks { position: absolute; inset: 0; }
  .crop-marks line { stroke: var(--crop); stroke-width: 1; }

  .card-front {
    position: absolute; left: 31px; top: 30px; width: 567px; height: 325px;
    background: radial-gradient(ellipse 70% 85% at 46% 46%, var(--card-light) 0%, var(--card-mid) 55%, var(--card-dark) 100%);
    overflow: hidden;
  }
  .head-silhouette {
    position: absolute; left: 34px; top: 110px; width: 170px; height: 215px;
    background: linear-gradient(180deg, var(--silhouette), #7d7b79);
    border-radius: 40% 45% 0 0 / 30% 34% 0 0;
  }
  .unisex-symbol {
    position: absolute; left: 500px; top: 28px; width: 42px; height: 42px;
    background: var(--ink-light); border-radius: 4px; opacity: .85;
  }
  .business-name {
    position: absolute; left: 228px; top: 222px;
    font-family: "Varela Round", sans-serif; font-weight: 400;
    font-size: 27px; line-height: 30px; letter-spacing: .3px;
    color: var(--ink-light); white-space: nowrap;
  }
  .contact {
    position: absolute; left: 228px; top: 262px;
    font-family: "Varela Round", sans-serif; font-size: 17px; line-height: 25px;
    color: var(--ink-light); letter-spacing: .3px; white-space: nowrap;
  }

  .card-back {
    position: absolute; left: 598px; top: 30px; width: 569px; height: 325px;
    background: var(--sheet); color: var(--ink-dark);
    font-family: "Arimo", Arial, sans-serif;
  }
  .appointment-title {
    position: absolute; top: 120px; width: 100%; text-align: center;
    font-size: 20px; font-weight: 700; letter-spacing: .3px;
  }
  .appointment-fields {
    position: absolute; left: 71px; top: 186px;
    display: flex; align-items: flex-end; gap: 6px;
    font-size: 17px; line-height: 20px; white-space: nowrap;
  }
  .field-line {
    display: inline-block; width: 162px; height: 17px;
    border-bottom: 1px solid var(--ink-dark); margin-right: 5px;
  }
</style>
</head>
<body>
<main class="print-sheet">
  <svg class="crop-marks" width="1200" height="383" aria-hidden="true">
    <line x1="0" y1="30.5" x2="19" y2="30.5"/>
    <line x1="0" y1="354.5" x2="19" y2="354.5"/>
    <line x1="31.5" y1="0" x2="31.5" y2="19"/>
    <line x1="31.5" y1="367" x2="31.5" y2="383"/>
    <line x1="598.5" y1="0" x2="598.5" y2="19"/>
    <line x1="598.5" y1="367" x2="598.5" y2="383"/>
    <line x1="1167.5" y1="0" x2="1167.5" y2="19"/>
    <line x1="1167.5" y1="367" x2="1167.5" y2="383"/>
    <line x1="1180" y1="30.5" x2="1200" y2="30.5"/>
    <line x1="1180" y1="354.5" x2="1200" y2="354.5"/>
  </svg>

  <section class="card-front">
    <div class="head-silhouette" role="img" aria-label="Grey side-profile head silhouette"></div>
    <div class="unisex-symbol" role="img" aria-label="Small unisex symbol"></div>
    <h1 class="business-name">Kestra Hair Design</h1>
    <p class="contact">318 Marlowe Road Pennick.<br>Ph (09) 4162093</p>
  </section>

  <section class="card-back">
    <h2 class="appointment-title">APPOINTMENT</h2>
    <p class="appointment-fields">
      <span>Time:</span><span class="field-line"></span>
      <span>Date:</span><span class="field-line"></span>
    </p>
  </section>
</main>
</body>
</html>
```